TECH PROJECT NEEDS NEW SKINS FOR RE-BRANDING

We are a technology project that has a product (crypto wallet) nearing release, have basic designs made so far however we need NEW SKINS/ branding/ design options for this wallet to change the look and feel -- it will be called and re-branded as "NOVAK" a futuristic/ space/ edgy product so need it to look like so.

YOU ARE ALLOWED TO CHANGE + EXPERIMENT WITH THE LAYOUT/ schema and UI as you see fit -- (we are open to new and creative ideas)

(see WALLET.PNG and PROTFOLIO.PNG ATTACHED --- these are the pages we need new skins for )

(see NOVAK logo attached --- PLEASE USE THIS LOGO/ VERSIONS OF THIS LOGO IN YOUR DESIGNS/SKIN SUBMISSIONS -- WE PROVIDED THE ai file so feel free to alter the logo a bit to experiment if you want -- we are open and flexible to new creative ideas)

(FOR A MOOD BOARD FOR GUIDANCE on feel/colors/mood-- SEE "SAMPLE INTERFACE 1 & 2" ATTACHED)

Target Market(s)

TECHNOLOGY/SPACE/ FUTURE

Number of Pages Required

2 page

Colors

Designer to choose colors to be used in the design.

Requirements
Must have
• MUST USE OUR NOVAK LOGO OR A SIMILAR ALTERATION OF IT

```html
<!DOCTYPE html>
<html lang="en">
<head>
<meta charset="utf-8">
<title>NOVAK Wallet Dashboard</title>
<link href="https://fonts.googleapis.com/css2?family=Nunito+Sans:wght@300;400;600;700&display=swap" rel="stylesheet">
<style>
:root{
  --bg-main:#2d2f38;
  --bg-side:#25272f;
  --bg-row:#25262d;
  --line:#353740;
  --text:#f2f3f6;
  --text-dim:#c3c5cc;
  --text-faint:#6d707a;
  --accent:#4be0a8;
  --green:#3fd28b;
  --purple:#8d6fe0;
  --red:#ef4b55;
  --link:#8c6ff0;
  --gold:#f7b731;
  --blue:#5c7cf2;
}
*{box-sizing:border-box;margin:0;padding:0}
html,body{width:1200px;height:854px;overflow:hidden}
body{background:var(--bg-main);font-family:"Nunito Sans",sans-serif;color:var(--text);position:relative}
.sidebar{position:absolute;left:0;top:0;width:181px;height:854px;background:var(--bg-side)}
.brand{position:absolute;left:0;width:181px;top:18px;display:flex;justify-content:center;align-items:center;gap:7px;color:var(--accent);font-weight:700;font-size:15px;letter-spacing:2px}
.brand-dot{width:11px;height:11px;border-radius:50%;background:var(--accent)}
.side-rule{position:absolute;left:18px;right:16px;top:58px;height:1px;background:var(--line)}
.quick{position:absolute;left:19px;top:73px;font-size:15px;font-weight:600}
.nav-item{position:absolute;left:16px;display:flex;align-items:center;gap:8px;font-size:11px;font-weight:700}
.nav-item svg{width:18px;height:18px;fill:none;stroke:var(--text);stroke-width:1.3}
.nav-active-bar{position:absolute;left:0;top:120px;width:4px;height:32px;background:var(--accent)}
.side-foot{position:absolute;left:0;width:181px;top:820px;height:1px;background:var(--line)}
.logout{top:827px}
.logout svg{stroke:var(--blue)}
.topbar svg{position:absolute;fill:none;stroke:var(--text-dim);stroke-width:1.3}
.search{position:absolute;left:294px;top:17px;width:200px;height:25px;border-radius:13px;background:#fff;display:flex;align-items:center;padding-left:9px;gap:6px;font-size:8px;color:#b8bac1}
.search svg{position:static;stroke:#444;width:14px;height:14px}
.avatar{position:absolute;left:1020px;top:16px;width:28px;height:28px;border-radius:50%;background:radial-gradient(circle,#b88a6d,#5a4538)}
.badge{position:absolute;left:1121px;top:16px;width:12px;height:12px;border-radius:50%;background:#ef5366;font-size:7px;text-align:center;line-height:12px;font-weight:700}
.flag{position:absolute;left:1151px;top:22px;width:16px;height:16px;border-radius:50%;background:linear-gradient(#c8374a 0 50%,#f2f2f2 50%);box-shadow:inset 8px 8px 0 -1px #2f3a7a}
.crumb{position:absolute;left:225px;top:79px;font-size:8.5px;color:var(--text-dim);display:flex;gap:5px;align-items:center}
.crumb b{color:var(--text);font-weight:700}
.crumb i{width:0;height:0;border-left:6px solid transparent;border-bottom:6px solid var(--blue)}
.card{position:absolute;top:138px;width:224px;height:91px;border-radius:8px;background:linear-gradient(160deg,#41434d,#34363f);box-shadow:0 4px 10px rgba(0,0,0,.25)}
.coin-dot{position:absolute;left:8px;top:8px;width:18px;height:18px;border-radius:50%}
.gold{background:var(--gold)}
.blu{background:var(--blue)}
.card-sym{position:absolute;left:37px;top:7px;font-size:12px;font-weight:700}
.card-name{position:absolute;left:37px;top:21px;font-size:8px;color:var(--text-faint)}
.card-price{position:absolute;right:10px;top:4px;font-size:12px}
.card-chg{position:absolute;right:10px;top:25px;font-size:8px}
.down{color:var(--red)}
.up{color:var(--green)}
.card svg{position:absolute;left:8px;top:34px}
.coins{position:absolute;left:208px;top:283px;width:956px;border-collapse:collapse;table-layout:fixed;font-size:13px}
.coins th{height:36px;background:var(--bg-row);text-align:left;font-weight:600;color:var(--text-dim)}
.coins th:first-child{padding-left:6px;color:var(--text);position:relative}
.coins th:first-child::after{content:"";position:absolute;left:2px;width:93px;bottom:-1px;height:2px;background:var(--green)}
.coins td{height:38.4px;font-weight:400;white-space:nowrap}
.coins tbody tr:nth-child(even) td{background:var(--bg-row)}
.name-cell{padding-left:6px;display:flex;align-items:center;gap:6px;height:38.4px}
.name-cell .coin-dot{position:static;width:16px;height:16px}
.chg{color:var(--red);display:flex;align-items:center;gap:10px;height:38.4px}
.chg::before{content:"";border-left:8px solid transparent;border-right:8px solid transparent;border-top:9px solid var(--red)}
.act{color:var(--link)}
.act span{color:var(--text);margin:0 3px}
.chat{position:absolute;left:1126px;top:800px;width:38px;height:37px;border-radius:6px;background:#1e2740;display:flex;align-items:center;justify-content:center;box-shadow:0 4px 10px rgba(0,0,0,.3)}
</style>
</head>
<body>
<aside class="sidebar">
  <div class="brand"><span class="brand-dot"></span>NOVAK</div>
  <div class="side-rule"></div>
  <div class="quick">Quick Access</div>
  <div class="nav-active-bar"></div>
  <div class="nav-item" style="top:127px;left:19px"><svg viewBox="0 0 18 18"><path d="M2 16h14M3 15l4-5 3 2 5-7M12 5h3v3"/></svg>Dashboard</div>
  <div class="nav-item" style="top:179px"><svg viewBox="0 0 18 18"><circle cx="9" cy="6" r="4"/><path d="M2 17c0-4 3-6 7-6s7 2 7 6z"/></svg>Portfolio</div>
  <div class="nav-item" style="top:233px"><svg viewBox="0 0 18 18"><rect x="1" y="4" width="16" height="11" rx="1"/><path d="M1 7h16M12 11h3"/></svg>My Wallet</div>
  <div class="nav-item" style="top:286px"><svg viewBox="0 0 18 18"><path d="M11 1L4 10h5l-2 7 7-9H9z"/></svg>Lightning</div>
  <div class="nav-item" style="top:340px"><svg viewBox="0 0 18 18"><path d="M5 14h9a3 3 0 0 0 0-6 5 5 0 0 0-9-1 3.5 3.5 0 0 0 0 7z"/></svg>ORB Cloud</div>
  <div class="side-foot"></div>
  <div class="nav-item logout"><svg viewBox="0 0 18 18"><path d="M9 1v8M5 4a7 7 0 1 0 8 0"/></svg>Log Out</div>
</aside>

<header class="topbar">
  <svg style="left:213px;top:21px" width="18" height="16" viewBox="0 0 18 16"><path d="M1 2h16M4 8h13M1 14h16"/></svg>
  <svg style="left:253px;top:20px" width="18" height="18" viewBox="0 0 18 18"><path d="M9 1l7 4v8l-7 4-7-4V5zM2 5l7 4 7-4M9 9v8"/></svg>
  <div class="search"><svg viewBox="0 0 14 14"><circle cx="6" cy="6" r="4.5"/><path d="M9.5 9.5L13 13"/></svg>Type any cryptocurrency...</div>
  <div class="avatar" role="img" aria-label="User profile photo"></div>
  <svg style="left:1110px;top:22px" width="18" height="16" viewBox="0 0 18 16"><path d="M2 6h3l8-4v12l-8-4H2zM5 10l1 4h2l-1-4"/></svg>
  <div class="badge">3</div>
  <div class="flag" role="img" aria-label="Language flag"></div>
</header>

<div class="crumb">Welcome <i></i><b>Dashboard</b><i></i></div>
<svg style="position:absolute;left:1114px;top:110px" width="8" height="12" viewBox="0 0 8 12" fill="none" stroke="#fff" stroke-width="1.4"><path d="M7 1L2 6l5 5"/></svg>
<svg style="position:absolute;left:1148px;top:110px" width="8" height="12" viewBox="0 0 8 12" fill="none" stroke="#fff" stroke-width="1.4"><path d="M1 1l5 5-5 5"/></svg>

<svg width="0" height="0" style="position:absolute">
  <defs>
    <linearGradient id="fillGreen" x1="0" y1="0" x2="0" y2="1"><stop offset="0" stop-color="#3fd28b" stop-opacity=".35"/><stop offset="1" stop-color="#3fd28b" stop-opacity="0"/></linearGradient>
    <linearGradient id="fillPurple" x1="0" y1="0" x2="0" y2="1"><stop offset="0" stop-color="#8d6fe0" stop-opacity=".4"/><stop offset="1" stop-color="#8d6fe0" stop-opacity="0"/></linearGradient>
  </defs>
</svg>

<div class="card" style="left:214px">
  <div class="coin-dot gold"></div><div class="card-sym">ZRC</div><div class="card-name">Zircon</div>
  <div class="card-price">$ 61046</div><div class="card-chg down">-4.66% ↓</div>
  <svg width="208" height="46" viewBox="0 0 208 46"><path d="M0 40C15 20 25 16 38 18S55 26 65 24 80 14 90 18 108 26 120 20 135 2 142 8 152 40 162 38 175 18 180 14 190 12 200 32V46H0Z" fill="url(#fillGreen)"/><path d="M0 40C15 20 25 16 38 18S55 26 65 24 80 14 90 18 108 26 120 20 135 2 142 8 152 40 162 38 175 18 180 14 190 12 200 32" fill="none" stroke="#3fd28b" stroke-width="1.3"/></svg>
</div>
<div class="card" style="left:456px">
  <div class="coin-dot blu"></div><div class="card-sym">QTM</div><div class="card-name">Quantum</div>
  <div class="card-price">¥ 22,370</div><div class="card-chg up">+0.45% ↑</div>
  <svg width="208" height="46" viewBox="0 0 208 46"><path d="M0 36C12 12 24 16 34 28S50 30 60 20 75 6 90 10 110 16 120 16 135 30 148 26 165 8 175 12 190 40 200 38 206 20 208 12V46H0Z" fill="url(#fillPurple)"/><path d="M0 36C12 12 24 16 34 28S50 30 60 20 75 6 90 10 110 16 120 16 135 30 148 26 165 8 175 12 190 40 200 38 206 20 208 12" fill="none" stroke="#8d6fe0" stroke-width="1.3"/></svg>
</div>
<div class="card" style="left:698px">
  <div class="coin-dot gold"></div><div class="card-sym">ZRC</div><div class="card-name">Zircon</div>
  <div class="card-price">$ 61046</div><div class="card-chg down">-4.66% ↓</div>
  <svg width="208" height="46" viewBox="0 0 208 46"><path d="M0 40C15 20 25 16 38 18S55 26 65 24 80 14 90 18 108 26 120 20 135 2 142 8 152 40 162 38 175 18 180 14 190 12 200 32V46H0Z" fill="url(#fillGreen)"/><path d="M0 40C15 20 25 16 38 18S55 26 65 24 80 14 90 18 108 26 120 20 135 2 142 8 152 40 162 38 175 18 180 14 190 12 200 32" fill="none" stroke="#3fd28b" stroke-width="1.3"/></svg>
</div>
<div class="card" style="left:939px">
  <div class="coin-dot blu"></div><div class="card-sym">QTM</div><div class="card-name">Quantum</div>
  <div class="card-price">¥ 22,370</div><div class="card-chg up">+0.45% ↑</div>
  <svg width="208" height="46" viewBox="0 0 208 46"><path d="M0 36C12 12 24 16 34 28S50 30 60 20 75 6 90 10 110 16 120 16 135 30 148 26 165 8 175 12 190 40 200 38 206 20 208 12V46H0Z" fill="url(#fillPurple)"/><path d="M0 36C12 12 24 16 34 28S50 30 60 20 75 6 90 10 110 16 120 16 135 30 148 26 165 8 175 12 190 40 200 38 206 20 208 12" fill="none" stroke="#8d6fe0" stroke-width="1.3"/></svg>
</div>

<table class="coins">
  <colgroup><col style="width:126px"><col style="width:100px"><col style="width:108px"><col style="width:94px"><col style="width:89px"><col style="width:117px"><col style="width:90px"><col style="width:84px"><col style="width:148px"></colgroup>
  <thead><tr><th>Coin Name</th><th>Market Cap</th><th>Volume 24 H</th><th>% Change</th><th>Last Price</th><th>Balance</th><th>Value</th><th>Portfolio</th><th>Action</th></tr></thead>
  <tbody>
    <tr><td><div class="name-cell"><span class="coin-dot gold"></span>Zircon-ZRC</div></td><td>120 B</td><td>2.5B</td><td><div class="chg">4.2%</div></td><td>$2999.50</td><td>10.000020 ZRC</td><td>$ 30000.4</td><td>12.43 %</td><td class="act">Send<span>|</span>Recieve</td></tr>
    <tr><td><div class="name-cell"><span class="coin-dot blu"></span>Quantum</div></td><td>120 B</td><td>2.5B</td><td><div class="chg">4.2%</div></td><td>$2999.50</td><td>10.000020 ZRC</td><td>$ 30000.4</td><td>12.43 %</td><td class="act">Send<span>|</span>Recieve</td></tr>
    <tr><td><div class="name-cell"><span class="coin-dot gold"></span>Zircon-ZRC</div></td><td>120 B</td><td>2.5B</td><td><div class="chg">4.2%</div></td><td>$2999.50</td><td>10.000020 ZRC</td><td>$ 30000.4</td><td>12.43 %</td><td class="act">Send<span>|</span>Recieve</td></tr>
    <tr><td><div class="name-cell"><span class="coin-dot blu"></span>Quantum</div></td><td>120 B</td><td>2.5B</td><td><div class="chg">4.2%</div></td><td>$2999.50</td><td>10.000020 ZRC</td><td>$ 30000.4</td><td>12.43 %</td><td class="act">Send<span>|</span>Recieve</td></tr>
    <tr><td><div class="name-cell"><span class="coin-dot gold"></span>Zircon-ZRC</div></td><td>120 B</td><td>2.5B</td><td><div class="chg">4.2%</div></td><td>$2999.50</td><td>10.000020 ZRC</td><td>$ 30000.4</td><td>12.43 %</td><td class="act">Send<span>|</span>Recieve</td></tr>
    <tr><td><div class="name-cell"><span class="coin-dot blu"></span>Quantum</div></td><td>120 B</td><td>2.5B</td><td><div class="chg">4.2%</div></td><td>$2999.50</td><td>10.000020 ZRC</td><td>$ 30000.4</td><td>12.43 %</td><td class="act">Send<span>|</span>Recieve</td></tr>
    <tr><td><div class="name-cell"><span class="coin-dot gold"></span>Zircon-ZRC</div></td><td>120 B</td><td>2.5B</td><td><div class="chg">4.2%</div></td><td>$2999.50</td><td>10.000020 ZRC</td><td>$ 30000.4</td><td>12.43 %</td><td class="act">Send<span>|</span>Recieve</td></tr>
    <tr><td><div class="name-cell"><span class="coin-dot blu"></span>Quantum</div></td><td>120 B</td><td>2.5B</td><td><div class="chg">4.2%</div></td><td>$2999.50</td><td>10.000020 ZRC</td><td>$ 30000.4</td><td>12.43 %</td><td class="act">Send<span>|</span>Recieve</td></tr>
    <tr><td><div class="name-cell"><span class="coin-dot gold"></span>Zircon-ZRC</div></td><td>120 B</td><td>2.5B</td><td><div class="chg">4.2%</div></td><td>$2999.50</td><td>10.000020 ZRC</td><td>$ 30000.4</td><td>12.43 %</td><td class="act">Send<span>|</span>Recieve</td></tr>
    <tr><td><div class="name-cell"><span class="coin-dot blu"></span>Quantum</div></td><td>120 B</td><td>2.5B</td><td><div class="chg">4.2%</div></td><td>$2999.50</td><td>10.000020 ZRC</td><td>$ 30000.4</td><td>12.43 %</td><td class="act">Send<span>|</span>Recieve</td></tr>
    <tr><td><div class="name-cell"><span class="coin-dot gold"></span>Zircon-ZRC</div></td><td>120 B</td><td>2.5B</td><td><div class="chg">4.2%</div></td><td>$2999.50</td><td>10.000020 ZRC</td><td>$ 30000.4</td><td>12.43 %</td><td class="act">Send<span>|</span>Recieve</td></tr>
    <tr><td><div class="name-cell"><span class="coin-dot blu"></span>Quantum</div></td><td>120 B</td><td>2.5B</td><td><div class="chg">4.2%</div></td><td>$2999.50</td><td>10.000020 ZRC</td><td>$ 30000.4</td><td>12.43 %</td><td class="act">Send<span>|</span>Recieve</td></tr>
  </tbody>
</table>

<div class="chat"><svg width="16" height="15" viewBox="0 0 16 15"><path d="M1 1h14v10H5l-4 3z" fill="#4b8cf5"/></svg></div>
</body>
</html>
```